Fennick Grove Gummy Bottle Label Design

(see attached word doc for full project description and example labels we like)
PROJECT OVERVIEW:
Fennick Grove is a healthy blend of functional organic super mushroom gummies that aims to enhance mood and promote overall mental and physical well-being by taking daily doses. The gummy product line offers a range of benefits, including increased energy, focus, calmness, sleep, immunity defense and overall mood upliftment. Fennick Grove is a brand that exudes positivity, vitality and personal growth. Fennick Grove is accessible, friendly, and approachable, making it easy for customers to integrate the brand into their daily routine. We cater/celebrate self-care by tending to both mental health and physical health.

Each benefit (i.e. product & flavor) is assigned a specific color that represents that “mood.” There are a total of 6 Moods, all 6 colors must be cohesive together. We prefer the color that represents the Mood to also be a clear representation of the flavor assigned to that mood, but we are open to interpretation if the color story looks good. We are also open to imagery (either real images or flaticons representing the ingredients or flavors) on the labels to help illustrate the components of this delicious product.

LABEL REQUEST:
The Fennick Grove products are gummies that will be placed in bottles and bags. There will be 6 different products with designated moods and flavors (i.e. Sleep/Lavender Vanilla, Calm/blackberry, Uplift/Pineapple, Focus/peach, Defense/black cherry, Energy/orange).

Dimensions will vary, here are a few:
Bottles:
6" W x 2" H
5" W x 2" H

Pouches:
4 x 6 x 2"

PRODUCTS:

Uplifting
Flavor: Pineapple
Mood: Mood Enhancement, Mental Health Helper
Front Label Ingredients: Cordyceps
Back Label Ingredients: Magnesium, Vitamin B2, Theacrine, Rhodiola Rosea, Shiitake, Cordyceps, Myrcene, Pinene.

Focus
Flavor: Sunny Plume
Mood: Focused, Creative, Productive
Front Label Ingredients: Lion’s Mane & Cordyceps
Back Label Ingredients: Rhodiola Rosea, Theacrine, Luteolin, Forskolin, Lions Mane, Cordyceps, Caryphyllene, Linalool.

Defense
Flavor: Black Cherry
Mood: Immunity & Gut Health
Front Label Ingredients: Turkey Tail
Back Label Ingredients: Vit A, Vit C, Ginger, Magnesium Glycinate, Lemon Balm, Maitake, Turkey Tail, Humulene.

Energy
Flavor: Rocket Parade
Mood: Awake, Stamina, Active
Front Label Ingredients: Lions Mane & Cordyceps
Back Label Ingredients: (NALT) N-Acetylcysteine-L-Tyrosine NALT, Caffeine, Vitamin B1, B3, Rhodiola Rosea, Ginkgo, Cordyceps, Valencene, Lions Mane, Limonene.

Sleep
Flavor: Vanilla Lavender Marlow Tide blend
Mood: Bedtime, Naptime, Relax Time
Front Label Ingredients: Melatonin & Reishi
Back Label Ingredients: Melatonin, Ashwagandha, Reishi, Bobinsana, Passion Flower, Linalool.

Calm
Flavor: Juniper Reel
Mood: Chill, Relaxed, Good Vibes
Front Label Ingredients: Reishi & Ashwagandha
Back Label Ingredients: Ashwagandha, Lemon Balm, Reishi, Chamomile, Velvet Bean, Caryophyllene.

```html
<!DOCTYPE html>
<html lang="en">
<head>
<meta charset="utf-8">
<title>Fennick Grove Gummy Labels</title>
<link rel="stylesheet" href="https://fonts.googleapis.com/css2?family=Luckiest+Guy&family=Fredoka:wght@500;600&family=Montserrat:wght@800&display=swap">
<style>
  :root {
    --backdrop: #cfcfcf;
    --label-black: #1c1c1d;
    --label-edge: #2a2a2b;
    --ink-white: #f4f4f4;
    --peach: #ef7f63;
    --peach-deep: #d9603f;
    --pineapple: #ecd040;
    --pineapple-deep: #c9a62a;
    --cherry: #b3202a;
    --cherry-deep: #7e1018;
  }
  * { box-sizing: border-box; margin: 0; padding: 0; }
  html, body { width: 1200px; height: 903px; overflow: hidden; }
  body {
    background: var(--backdrop);
    font-family: "Fredoka", sans-serif;
    display: flex;
    align-items: center;
    justify-content: center;
    gap: 30px;
  }
  .label {
    position: relative;
    width: 360px;
    height: 450px;
    background: radial-gradient(circle at 50% 35%, var(--label-edge), var(--label-black) 70%);
    color: var(--ink-white);
    overflow: hidden;
  }
  .label--focus { --accent: var(--peach); --accent-deep: var(--peach-deep); }
  .label--uplift { --accent: var(--pineapple); --accent-deep: var(--pineapple-deep); }
  .label--defense { --accent: var(--cherry); --accent-deep: var(--cherry-deep); }

  .brand {
    position: absolute;
    top: 30px;
    left: 0; right: 0;
    display: flex;
    align-items: center;
    justify-content: center;
    gap: 8px;
    font-weight: 600;
    font-size: 24px;
    letter-spacing: 1px;
    text-transform: uppercase;
  }
  .brand-dot {
    width: 13px; height: 13px;
    border-radius: 50%;
    background: var(--ink-white);
  }
  .splash {
    position: absolute;
    top: 92px;
    left: 50%;
    transform: translateX(-50%);
    width: 270px;
    height: 190px;
    border-radius: 48% 52% 44% 56% / 55% 45% 55% 45%;
    background: radial-gradient(circle at 50% 35%, var(--accent-deep) 0 36%, transparent 72%);
    opacity: 0.9;
  }
  .mood-name {
    position: absolute;
    top: 112px;
    left: 0; right: 0;
    text-align: center;
    font-family: "Luckiest Guy", "Fredoka", sans-serif;
    font-weight: 400;
    font-size: 58px;
    line-height: 1;
    color: var(--ink-white);
    -webkit-text-stroke: 3px var(--accent);
    paint-order: stroke fill;
    text-shadow: 0 5px 0 var(--accent-deep);
    letter-spacing: 1px;
  }
  .flavor {
    position: absolute;
    top: 198px;
    left: 0; right: 0;
    text-align: center;
    font-family: "Luckiest Guy", "Fredoka", sans-serif;
    font-size: 32px;
    line-height: 1;
    color: var(--accent);
    -webkit-text-stroke: 1.5px var(--ink-white);
    paint-order: stroke fill;
  }
  .benefit-frame {
    position: absolute;
    top: 0; left: 0;
    width: 360px;
    height: 450px;
    pointer-events: none;
  }
  .benefit-frame path {
    fill: none;
    stroke: var(--ink-white);
    stroke-width: 1.5;
  }
  .benefits {
    position: absolute;
    top: 284px;
    left: 50%;
    transform: translateX(-50%);
    display: flex;
    align-items: center;
    gap: 10px;
    white-space: nowrap;
  }
  .flavor-icon {
    flex: none;
    width: 48px; height: 48px;
    border-radius: 50%;
    border: 2px solid var(--ink-white);
  }
  .benefit-list {
    font-weight: 500;
    font-size: 14px;
    line-height: 1.3;
    text-transform: uppercase;
  }
  .ingredients {
    position: absolute;
    top: 350px;
    left: 0; right: 0;
    text-align: center;
    font-weight: 500;
    font-size: 14px;
    text-transform: uppercase;
  }
  .count {
    position: absolute;
    top: 366px;
    left: 0; right: 0;
    text-align: center;
    font-family: "Montserrat", sans-serif;
    font-weight: 800;
    font-size: 28px;
    line-height: 1.1;
    color: var(--accent);
    text-transform: uppercase;
  }
  .stripe {
    position: absolute;
    left: 0; right: 0;
    top: 404px;
    height: 11px;
    background: var(--accent);
  }
</style>
</head>
<body>

  <section class="label label--focus">
    <div class="brand"><span class="brand-dot"></span>Fennick Grove</div>
    <div class="splash" role="img" aria-label="Peach coloured paint splash with halftone dots"></div>
    <svg class="benefit-frame" viewBox="0 0 360 450" aria-hidden="true">
      <path d="M86 214 H58 V309 H74 M286 309 H302 V214 H274"/>
    </svg>
    <h2 class="mood-name">Focus</h2>
    <p class="flavor">Sunny Plume</p>
    <div class="benefits">
      <div class="flavor-icon" role="img" aria-label="Line icon of a halved peach"></div>
      <p class="benefit-list">Focused, Creative<br>Productive</p>
    </div>
    <p class="ingredients">Lion’s Mane &amp; Cordyceps</p>
    <p class="count">50 Gummies</p>
    <div class="stripe"></div>
  </section>

  <section class="label label--uplift">
    <div class="brand"><span class="brand-dot"></span>Fennick Grove</div>
    <div class="splash" role="img" aria-label="Yellow paint splash with halftone dots"></div>
    <svg class="benefit-frame" viewBox="0 0 360 450" aria-hidden="true">
      <path d="M86 214 H58 V309 H72 M288 309 H302 V214 H274"/>
    </svg>
    <h2 class="mood-name">Uplifting</h2>
    <p class="flavor">Pineapple</p>
    <div class="benefits">
      <div class="flavor-icon" role="img" aria-label="Line icon of a pineapple with a slice"></div>
      <p class="benefit-list">Mood Enhancement<br>Mental Health Helper</p>
    </div>
    <p class="ingredients">Cordyceps</p>
    <p class="count">50 Gummies</p>
    <div class="stripe"></div>
  </section>

  <section class="label label--defense">
    <div class="brand"><span class="brand-dot"></span>Fennick Grove</div>
    <div class="splash" role="img" aria-label="Dark red paint splash with halftone dots"></div>
    <svg class="benefit-frame" viewBox="0 0 360 450" aria-hidden="true">
      <path d="M76 214 H58 V309 H110 M250 309 H302 V214 H284"/>
    </svg>
    <h2 class="mood-name">Defense</h2>
    <p class="flavor">Black Cherry</p>
    <div class="benefits">
      <div class="flavor-icon" role="img" aria-label="Line icon of a pair of cherries"></div>
      <p class="benefit-list">Immunity<br>Gut Health</p>
    </div>
    <p class="ingredients">Turkey Tail</p>
    <p class="count">50 Gummies</p>
    <div class="stripe"></div>
  </section>

</body>
</html>
```